Vesprine Oakville Cabernet Sauvignon-Wine label design

We need a package design for an up market wine brand named, Vesprine. It will be a Cabernet Sauvignon from the Oakville AVA of Napa Valley. We are looking for a stylish modern label that will stand out on a retail shelf. We want the label to be attention grabbing and stylish while presenting an up market luxury brand.

Sick

Requirements
Must have
• Must have the words(in order of importance)
-Vesprine
-Cabernet Sauvignon
-Oakville
-Napa Valley
-2018

Must be designed for a traditional "Bordeaux" style bottle (Bottle specs in uploaded files)
Should not have
• Any images of grapes, vineyards, wine glasses or bottles

```html
<!DOCTYPE html>
<html lang="en">
<head>
<meta charset="utf-8">
<title>Vesprine Oakville Cabernet Sauvignon Label</title>
<link href="https://fonts.googleapis.com/css2?family=Old+Standard+TT:wght@400&display=swap" rel="stylesheet">
<style>
  :root {
    --backdrop: #ebebeb;
    --label-black: #1d1d1d;
    --pattern-tone: #262626;
    --copper: #e3a47c;
    --copper-light: #f4c3a0;
    --copper-deep: #c9855c;
  }
  * { margin: 0; padding: 0; box-sizing: border-box; }
  html, body {
    width: 1200px;
    height: 960px;
    overflow: hidden;
    background: var(--backdrop);
  }
  .canvas {
    position: relative;
    width: 1200px;
    height: 960px;
  }
  .label {
    position: absolute;
    left: 350px;
    top: 50px;
    width: 500px;
    height: 860px;
    overflow: hidden;
    background: var(--label-black);
    font-family: "Old Standard TT", serif;
    color: var(--copper);
    text-align: center;
  }
  .label-pattern {
    position: absolute;
    left: 0;
    top: 28px;
    width: 100%;
    height: 790px;
    background: radial-gradient(ellipse at center, var(--pattern-tone) 0%, var(--label-black) 75%);
  }
  .trim {
    position: absolute;
    left: 0;
    width: 100%;
    background: linear-gradient(90deg, var(--copper-deep), var(--copper-light) 50%, var(--copper-deep));
  }
  .trim--top-outer { top: 4px; height: 6px; }
  .trim--top-inner { top: 18px; height: 4px; }
  .trim--bottom-inner { top: 822px; height: 4px; }
  .trim--bottom-outer { top: 838px; height: 6px; }
  .line {
    position: absolute;
    left: 0;
    width: 100%;
    line-height: 1;
    white-space: nowrap;
  }
  .brand-name {
    top: 166px;
    font-size: 84px;
    font-weight: 400;
    letter-spacing: 3px;
    padding-left: 3px;
  }
  .appellation {
    top: 386px;
    font-size: 31px;
    letter-spacing: 3px;
    padding-left: 3px;
  }
  .region {
    top: 438px;
    display: flex;
    align-items: center;
    gap: 20px;
    font-size: 31px;
    letter-spacing: 3px;
  }
  .region-name { flex: none; }
  .region-rule {
    flex: 1;
    height: 2px;
    background: var(--copper);
  }
  .varietal {
    top: 514px;
    font-size: 33px;
    letter-spacing: 3px;
    padding-left: 3px;
  }
  .vintage {
    top: 572px;
    font-size: 32px;
    letter-spacing: 2px;
    padding-left: 2px;
  }
  .volume {
    top: 770px;
    font-size: 34px;
    letter-spacing: 1px;
  }
</style>
</head>
<body>
<main class="canvas">
  <section class="label">
    <div class="label-pattern" role="img" aria-label="Faint dark damask ornament pattern across the label"></div>
    <div class="trim trim--top-outer"></div>
    <div class="trim trim--top-inner"></div>
    <h1 class="line brand-name">VESPRINE</h1>
    <p class="line appellation">OAKVILLE</p>
    <p class="line region"><span class="region-rule"></span><span class="region-name">NAPA VALLEY</span><span class="region-rule"></span></p>
    <p class="line varietal">CABERNET SAUVIGNON</p>
    <p class="line vintage">2018</p>
    <p class="line volume">750 ml</p>
    <div class="trim trim--bottom-inner"></div>
    <div class="trim trim--bottom-outer"></div>
  </section>
</main>
</body>
</html>
```